Beacon Advisory Website

I currently have a website www.beaconadvisoryinc.example. We are a IT Consulting Company. Our website will pretty much tell out our services. I am looking to enhance my website and make it look more professional. Looking for very classy and Contemporary look and design for my website.

Industry/Entity Type

It Company

```html
<!DOCTYPE html>
<html lang="en">
<head>
<meta charset="utf-8">
<title>Beacon Advisory</title>
<link href="https://fonts.googleapis.com/css2?family=Open+Sans:wght@300;400;600;700&display=swap" rel="stylesheet">
<style>
:root{
  --navy:#0d3a7e;
  --navy-deep:#0a2f6b;
  --cyan:#12a5e0;
  --ink:#333;
  --body:#555;
  --grey-bar:#555;
  --footer:#2d2d2d;
  --line:#d0d0d0;
}
*{margin:0;padding:0;box-sizing:border-box}
html,body{width:723px;height:1200px;overflow:hidden}
body{position:relative;font-family:'Open Sans',sans-serif;background:#fff;color:var(--ink)}
.abs{position:absolute}
.topbar{left:0;top:0;width:723px;height:51px;background:linear-gradient(90deg,#0b5cab,#0a56a5)}
.topbar-accent{left:0;top:0;width:186px;height:51px;background:var(--cyan)}
.social{top:6px;display:flex;gap:6px;left:68px}
.social span{width:13px;height:13px;border-radius:50%;background:#fff;display:block}
.topline{top:9px;font-size:7.5px;color:#fff;white-space:nowrap}
.header{left:60px;top:26px;width:604px;height:50px;background:#fff}
.brand{left:8px;top:12px;display:flex;align-items:center;gap:6px}
.brand i{width:24px;height:24px;background:var(--navy);display:block}
.brand b{font-size:13px;font-weight:700;color:var(--navy);line-height:1}
.nav{top:16px;font-size:8.2px;color:#222;letter-spacing:.2px}
.nav.active{background:var(--navy);color:#fff;padding:5px 10px;top:16px}
.hero{left:0;top:51px;width:723px;height:343px;background:linear-gradient(90deg,#f3f5f7 0%,#e6ebef 40%,#c9d3dc 65%,#7f8a96 100%)}
.hero-title{left:60px;top:134px;font-size:29px;line-height:32px;color:#555;font-weight:300}
.hero-title strong{color:var(--navy);font-weight:700}
.hero-sub{left:61px;top:208px;font-size:13.5px;color:#555;font-weight:300}
.btn{left:60px;top:242px;width:115px;height:34px;background:var(--cyan);color:#fff;font-size:12.5px;display:flex;align-items:center;padding-left:17px;gap:10px;font-weight:300}
.btn svg{width:14px;height:14px}
.h2{width:723px;left:0;text-align:center;font-size:27px;font-weight:600}
.rule{height:1px;background:var(--line)}
.mark{width:10px;height:10px;background:var(--cyan);border-radius:2px}
.intro{left:76px;top:492px;width:571px;font-size:9.5px;line-height:15.5px;color:var(--body);text-align:center}
.card{top:641px;width:160px;height:112px;border:1px solid #ddd;border-left:4px solid var(--grey-bar);background:#fff;padding:15px 0 0 27px}
.card.alt{background:#eee;border-color:#eee;border-left-color:var(--grey-bar)}
.card h3{font-size:14px;font-weight:400;color:#444;margin-bottom:6px}
.card p{font-size:7.4px;line-height:12.3px;color:#555;width:125px}
.card a{display:block;font-size:7.2px;color:#333;margin-top:5px;text-decoration:none}
.icon{width:48px;height:48px;border-radius:50%;display:flex;align-items:center;justify-content:center}
.contact{left:0;top:822px;width:723px;height:344px;background:linear-gradient(135deg,#12468f,#0a3478 60%,#093070)}
.map{left:60px;top:934px;width:268px;height:183px;background:linear-gradient(135deg,#e8e4dc,#dcd8cf)}
.company{left:349px;top:924px;font-size:18px;color:#fff;font-weight:600}
.office h4{font-size:10.5px;color:#fff;font-weight:600;margin-bottom:9px}
.row{display:flex;gap:6px;font-size:8px;line-height:10.3px;color:#fff;margin-bottom:8px}
.pin{width:13px;height:13px;border-radius:50%;background:var(--cyan);flex:none;display:flex;align-items:center;justify-content:center}
.pin svg{width:7px;height:7px}
.divider-v{left:494px;top:964px;width:1px;height:164px;background:rgba(255,255,255,.18)}
.divider-h{left:494px;top:1048px;width:138px;height:1px;background:rgba(255,255,255,.18)}
.footer{left:0;top:1166px;width:723px;height:34px;background:var(--footer);color:#bbb;font-size:8px;text-align:center;line-height:34px}
</style>
</head>
<body>
<div class="abs topbar"></div>
<div class="abs topbar-accent"></div>
<div class="abs social"><span></span><span></span><span></span><span></span><span></span></div>
<div class="abs topline" style="left:258px">Meeting these demands for over 25 years</div>
<div class="abs topline" style="left:424px">Talk With Us &nbsp;☏ +1 (555) 014 2290 &nbsp;&nbsp;| &nbsp;✉ info@beaconadvisory.example</div>

<div class="abs hero" role="img" aria-label="Photo of two business people reviewing a tablet at a desk"></div>
<header class="abs header">
  <div class="abs brand"><i></i><b>BEACON<br>ADVISORY</b></div>
  <span class="abs nav active" style="left:213px">HOME</span>
  <span class="abs nav" style="left:275px">SERVICES</span>
  <span class="abs nav" style="left:338px">SOLUTIONS</span>
  <span class="abs nav" style="left:410px">RESOURCES</span>
  <span class="abs nav" style="left:484px">CAREER</span>
  <span class="abs nav" style="left:542px">CONTACT US</span>
</header>
<h1 class="abs hero-title"><strong>Today’s IT</strong> market<br>is a Dynamic</h1>
<p class="abs hero-sub">Meeting these demands for over 25 years</p>
<a class="abs btn">View More <svg viewBox="0 0 14 14"><circle cx="7" cy="7" r="7" fill="#0d3a7e"/><path d="M6 4l3 3-3 3" stroke="#fff" stroke-width="1.5" fill="none"/></svg></a>

<h2 class="abs h2" style="top:420px;color:#333">What We Do</h2>
<div class="abs rule" style="left:160px;top:472px;width:438px"></div>
<div class="abs mark" style="left:363px;top:467px"></div>
<p class="abs intro">Today’s IT market is a dynamic, fast-paced industry, with ever-increasing demands. Meeting these demands for over 25 years, Beacon Advisory maintains a global presence, aggressively recruiting expertly qualified IT and Management Professionals from around the world and cultivating key partnerships with corporations to understand their business models end-to-end, with a goal of delivering exceptional client service and ensuring a consistent delivery of the talent needed to drive results.</p>
<svg class="abs" style="left:180px;top:580px" width="363" height="16" viewBox="0 0 363 16"><defs><linearGradient id="sh" x1="0" x2="1"><stop offset="0" stop-color="#fff"/><stop offset=".5" stop-color="#e4e4e4"/><stop offset="1" stop-color="#fff"/></linearGradient></defs><path d="M0 6H170l11 8 11-8H363" stroke="url(#sh)" stroke-width="3" fill="none"/></svg>

<div class="abs card" style="left:83px"><h3>Consulting</h3><p>Beacon Advisory has certified professional consultants to work with you to help increase the business by providing IT services ...</p><a>Read more →</a></div>
<div class="abs card alt" style="left:293px"><h3>Staff Augmentation</h3><p>For years Beacon Advisory as been offering our customers the ability to augment their existing staff ...</p><a>Read more →</a></div>
<div class="abs card" style="left:505px"><h3>Offshore</h3><p>Our Offshore development model has a unique distinction of providing efficient software solutions ...</p><a>Read more →</a></div>
<div class="abs icon" style="left:60px;top:673px;background:var(--cyan)"><svg width="24" height="22" viewBox="0 0 24 22" fill="none" stroke="#fff" stroke-width="1.5"><rect x="5" y="2" width="17" height="12" rx="1"/><path d="M2 6v11h4v3l3-3h9"/></svg></div>
<div class="abs icon" style="left:269px;top:673px;background:var(--navy)"><svg width="26" height="26" viewBox="0 0 26 26" fill="none" stroke="#fff" stroke-width="1.5"><circle cx="13" cy="13" r="11"/><circle cx="13" cy="11" r="3"/><path d="M8 20c1-3 3-4 5-4s4 1 5 4"/></svg></div>
<div class="abs icon" style="left:480px;top:673px;background:var(--navy-deep)"><svg width="26" height="26" viewBox="0 0 26 26" fill="none" stroke="#fff" stroke-width="1.8"><circle cx="13" cy="13" r="4"/><circle cx="13" cy="13" r="9" stroke-dasharray="4 2.5"/></svg></div>

<section class="abs contact" role="img" aria-label="Faint photo of a team at work under a blue overlay"></section>
<h2 class="abs h2" style="top:842px;color:#fff">Contact Us</h2>
<div class="abs rule" style="left:161px;top:891px;width:438px;background:rgba(255,255,255,.25)"></div>
<div class="abs mark" style="left:364px;top:886px;background:#fff"></div>
<div class="abs map" role="img" aria-label="Street map showing the technical center location"></div>
<div class="abs company">Beacon Advisory Inc.</div>
<div class="abs divider-v"></div>
<div class="abs divider-h"></div>

<div class="abs office" style="left:351px;top:963px">
  <h4>Head Office</h4>
  <div class="row"><span class="pin"><svg viewBox="0 0 8 8"><circle cx="4" cy="4" r="2" fill="#fff"/></svg></span><span>410 Harbor Lane<br>Suite 120<br>Eastfield, NJ 07000</span></div>
  <div class="row" style="margin-top:4px"><span class="pin"><svg viewBox="0 0 8 8"><path d="M2 1l1.5 2-1 1c.5 1 1 1.5 2 2l1-1 2 1.5-1 1.5C3 7.5.5 5 .5 2z" fill="#fff"/></svg></span><span style="line-height:13px">Phone: +1 (555) 014 2290</span></div>
</div>
<div class="abs office" style="left:513px;top:963px">
  <h4>West Coast Office</h4>
  <div class="row"><span class="pin"><svg viewBox="0 0 8 8"><circle cx="4" cy="4" r="2" fill="#fff"/></svg></span><span>88 Summit Way<br>Suite 300<br>Westbrook, CA 95000</span></div>
</div>
<div class="abs office" style="left:351px;top:1061px">
  <h4>Technical Center</h4>
  <div class="row"><span class="pin"><svg viewBox="0 0 8 8"><circle cx="4" cy="4" r="2" fill="#fff"/></svg></span><span>2700 Ridge Road<br>Suite 210<br>Millbrook MI 48000</span></div>
</div>

<footer class="abs footer">Copyright © 2007 - 2016 Beacon Advisory Ltd.&nbsp; All Rights Reserved</footer>
</body>
</html>
```